A web site for my wholesale/retail cleaning supplies company

I need a website that can accept payment from retail and wholesale customers. A good example is fresh meadow goods website. My company name is bright leaf northern. We will be selling sanitizers, all purpose cleaners, soaps and things of the such. All natural stuff.
Updates

Please focus on hand sanitizer as well. That will actually be my first product. Contact number 4035550187 email brightleafnorthern@mailbox-example.com for contact Facebook is www.socialpage-example.com/brightleafnorthern

Coding

Coded - Design and coding required

Number of Pages Required

1 page

Requirements
Must have
• Wholesale
Retail
Both in seperate sections.
Instagram brightleafnorthern
Facebook www.socialpage-example.com/brightleafnorthern
Email brightleafnorthern@mailbox-example.com
Number 4035550187

About us

Bright Leaf Northern is %100 canada based. We believe in building local communities and business together with locally sourced ingredients. As well as making safe alternatives to the harsh chemicals we are exposed to every day during simple tasks. Many cleaning supplies or household products can irritate the eyes or throat, or cause headaches and other health problems, including cancer. Some products release dangerous chemicals, including volatile organic compounds (VOC's). We find this to be not only uneccisary but widely dangerous. Join the "Spread" as we naturally cruise through canada creating healthier families everywhere.

```html
<!DOCTYPE html>
<html lang="en">
<head>
<meta charset="utf-8">
<title>Bright Leaf Northern – Natural Cleaning Supplies</title>
<link href="https://fonts.googleapis.com/css2?family=Poppins:wght@400;500;600;700&display=swap" rel="stylesheet">
<style>
:root{
  --green:#7cb82f;
  --green-dark:#5f9a1c;
  --blue:#1a8fd6;
  --blue-dark:#1479b8;
  --ink:#222b33;
  --nav:#26313a;
  --footer:#1f272e;
  --footer-deep:#171d22;
  --muted:#7b858d;
  --line:#e3e7ea;
  --soft:#f3f6f8;
  --white:#ffffff;
  --price-old:#a5adb3;
  --red:#e2412f;
}
*{box-sizing:border-box;margin:0;padding:0}
html,body{width:1200px;height:2568px;overflow:hidden}
body{font-family:"Poppins",Arial,sans-serif;color:var(--ink);background:var(--white);position:relative}
.wrap{position:absolute;left:0;width:1200px}

/* top bar */
.topbar{top:0;height:32px;background:var(--white);border-bottom:1px solid var(--line);font-size:11px;color:var(--muted)}
.topbar .promo{position:absolute;left:0;right:0;top:9px;text-align:center}
.topbar .track{position:absolute;right:92px;top:4px;height:24px;padding:0 16px;background:var(--green);color:var(--white);font-size:11px;font-weight:600;line-height:24px}

/* header */
.header{top:32px;height:88px}
.brand{position:absolute;left:92px;top:22px;display:flex;align-items:center;gap:10px}
.brand .dot{width:40px;height:40px;border-radius:50%;background:var(--green)}
.brand .name{font-size:22px;font-weight:700;color:var(--blue);line-height:1.05;width:160px}
.header .contact{position:absolute;right:92px;top:28px;display:flex;align-items:center;gap:26px;font-size:11px;color:var(--muted)}
.header .phone{display:flex;align-items:center;gap:8px;font-size:24px;font-weight:600;color:var(--blue)}

/* nav */
.nav{top:120px;height:30px;background:var(--nav)}
.nav ul{list-style:none;display:flex;position:absolute;left:92px;top:0;height:30px}
.nav li{font-size:11px;font-weight:600;color:var(--white);padding:0 14px;line-height:30px;letter-spacing:.3px}
.nav li.active{background:var(--blue)}
.nav .search{position:absolute;right:92px;top:7px}

/* hero */
.hero{top:160px;height:360px}
.hero-main{position:absolute;left:92px;top:0;width:712px;height:360px;background:linear-gradient(90deg,#e9ecee 0%,#f2f4f5 50%,#dfe4e7 100%)}
.hero-main .photo{position:absolute;right:0;top:0;width:400px;height:360px;background:linear-gradient(160deg,#eef1f2,#d7dde1)}
.hero-main .copy{position:absolute;left:44px;top:110px}
.hero-main .tag{display:inline-block;background:var(--green);color:var(--white);font-size:11px;font-weight:600;padding:3px 10px}
.hero-main h1{font-size:40px;font-weight:600;color:var(--ink);margin-top:10px;line-height:1.1}
.hero-main .sub{font-size:11px;color:var(--muted);letter-spacing:.5px;margin-top:6px}
.btn{display:inline-block;font-size:10px;font-weight:600;color:var(--white);background:var(--blue);padding:7px 16px;letter-spacing:.4px}
.hero-main .btn{margin-top:26px}
.hero-dots{position:absolute;left:50%;bottom:16px;display:flex;gap:6px;transform:translateX(-50%)}
.hero-dots span{width:8px;height:8px;border-radius:50%;background:#c6cdd2}
.hero-dots span.on{background:var(--blue)}
.side{position:absolute;left:824px;width:284px}
.side-a{top:0;height:118px;background:linear-gradient(135deg,#e7eef0,#d4dee2)}
.side-a .label{position:absolute;left:0;top:0;width:120px;height:118px}
.side-a .txt{position:absolute;left:20px;top:30px}
.side-a .small{font-size:11px;font-weight:600;color:var(--muted)}
.side-a .big{font-size:24px;font-weight:600;color:var(--green);line-height:1.1}
.side-b{top:128px;height:108px;background:linear-gradient(135deg,#c9b596,#8e9b6a)}
.side-b .cap{position:absolute;left:118px;top:44px;font-size:12px;font-weight:600;color:var(--white)}
.side-c{top:246px;height:114px;background:linear-gradient(135deg,#2aa0e0,var(--blue-dark))}
.side-c .big{position:absolute;left:22px;top:24px;font-size:32px;font-weight:600;color:var(--white)}
.side-c .code{position:absolute;left:22px;top:72px;background:var(--white);color:var(--blue);font-size:10px;font-weight:600;padding:4px 10px}

/* categories */
.cats-bg{top:530px;height:520px;background:linear-gradient(180deg,#ffffff 0%,var(--soft) 100%)}
.section-title{position:absolute;left:0;width:1200px;text-align:center;font-size:22px;font-weight:600;color:var(--ink)}
.cats{position:absolute;left:168px;top:604px;display:flex;gap:22px}
.cat{width:202px;height:258px;background:var(--white);border:1px solid var(--line);position:relative;text-align:center}
.cat .photo{height:150px;background:linear-gradient(160deg,#e9eef0,#c9d3d8)}
.cat .icon{position:absolute;left:86px;top:132px;width:30px;height:30px;border-radius:50%;background:var(--green);display:flex;align-items:center;justify-content:center}
.cat h3{margin-top:24px;font-size:12px;font-weight:600}
.cat p{font-size:10px;color:var(--green);margin-top:2px}
.cat.feature{top:-12px;box-shadow:0 6px 18px rgba(0,0,0,.12)}
.cat.feature .btn{margin-top:10px}

/* featured */
.products{position:absolute;left:168px;top:1158px;display:flex;gap:14px}
.prod{width:162px;height:330px;background:var(--white);border:1px solid var(--line);position:relative;text-align:center}
.prod .photo{height:180px;margin:8px;background:linear-gradient(160deg,#f1f4f5,#dde3e6)}
.prod .badge{position:absolute;right:0;top:0;font-size:9px;font-weight:600;color:var(--white);padding:3px 8px}
.prod .badge.new{background:var(--blue)}
.prod .badge.sale{background:var(--red)}
.prod h4{font-size:10px;font-weight:600;line-height:1.4;padding:6px 18px 0}
.prod .price{margin-top:8px;font-size:14px;font-weight:600;color:var(--green)}
.prod .price s{font-size:11px;color:var(--price-old);font-weight:400;margin-left:6px}
.prod .actions{position:absolute;left:12px;right:12px;bottom:14px;display:flex;gap:6px}
.prod .actions .buy{flex:1;background:var(--green);color:var(--white);font-size:9px;font-weight:600;height:26px;line-height:26px}
.prod .actions .wish{width:30px;height:26px;border:1px solid var(--blue);display:flex;align-items:center;justify-content:center}
.prod.hover{box-shadow:0 6px 18px rgba(0,0,0,.12)}
.arrow{position:absolute;top:1312px;width:26px;height:26px;border-radius:50%;background:#d2d8dc;display:flex;align-items:center;justify-content:center}

/* promo band */
.promo-band{top:1568px;left:168px;width:864px;height:352px}
.promo-band .left{position:absolute;left:0;top:0;width:430px;height:352px;background:linear-gradient(135deg,#2ea3e2,var(--blue-dark));text-align:center;color:var(--white)}
.promo-band .mark{width:44px;height:44px;border-radius:50%;background:rgba(255,255,255,.9);margin:56px auto 12px}
.promo-band h2{font-size:24px;font-weight:600;letter-spacing:1px}
.promo-band .sub{font-size:13px;opacity:.9}
.promo-band .flat{font-size:12px;margin-top:22px}
.promo-band .off{font-size:40px;font-weight:600;line-height:1.1}
.promo-band .btn{background:var(--green);margin-top:14px}
.promo-band .right{position:absolute;left:430px;top:0;width:434px;height:352px;background:linear-gradient(160deg,#6b6f66,#2c2f2c 60%,#4a4038)}
.promo-band .inset{position:absolute;left:420px;top:-20px;width:150px;height:120px;background:linear-gradient(160deg,#3a4652,#1d2630);border:4px solid var(--white)}

/* features */
.features{position:absolute;left:168px;top:1984px;display:flex;gap:0}
.feat{width:216px;height:150px;border:1px solid var(--line);margin-right:-1px;text-align:center;padding-top:30px}
.feat .ic{height:40px;display:flex;align-items:center;justify-content:center}
.feat h5{font-size:11px;font-weight:600;margin-top:12px}
.feat p{font-size:9px;color:var(--muted);margin-top:2px}

/* footer */
.footer{top:2180px;height:348px;background:var(--footer);color:#c3cad0}
.footer .brand{left:168px;top:100px}
.footer .brand .name{color:var(--white)}
.footer h6{font-size:13px;font-weight:600;color:var(--white);margin-bottom:14px}
.footer .col{position:absolute;top:60px}
.footer .call{font-size:16px;font-weight:500;color:var(--white)}
.footer .mail{font-size:10px;margin-top:4px}
.footer .connect{font-size:10px;font-weight:600;color:var(--white);margin-top:26px}
.footer .social{display:flex;gap:8px;margin-top:10px}
.footer .social span{width:26px;height:26px;border-radius:50%;background:#3a454f}
.footer .social span.on{background:var(--blue)}
.footer .news p{font-size:10px;line-height:1.5;width:260px}
.footer .input{margin-top:12px;width:250px;height:30px;background:var(--white);font-size:10px;color:var(--muted);padding:8px 10px}
.footer .send{margin-top:10px;background:var(--green)}
.bottom{top:2528px;height:40px;background:var(--footer-deep);font-size:10px;color:#9aa3aa}
.bottom .copy{position:absolute;left:168px;top:13px}
.bottom .pay{position:absolute;right:168px;top:10px;display:flex;gap:6px}
.bottom .pay span{width:32px;height:20px;background:#d9dee2;border-radius:2px}
.to-top{position:absolute;right:24px;top:2536px;width:24px;height:24px;border-radius:50%;background:var(--green);display:flex;align-items:center;justify-content:center}
</style>
</head>
<body>

<div class="wrap topbar">
  <div class="promo">Free Shipping on Orders Over $99</div>
  <div class="track">Track Order</div>
</div>

<header class="wrap header">
  <div class="brand"><span class="dot"></span><span class="name">Bright Leaf Northern</span></div>
  <div class="contact">
    <span>GET YOUR FREE PROMO CODE NOW</span>
    <span class="phone">
      <svg width="22" height="22" viewBox="0 0 24 24"><path fill="#1a8fd6" d="M6.6 10.8a15 15 0 0 0 6.6 6.6l2.2-2.2c.3-.3.7-.4 1-.2 1.1.4 2.3.6 3.6.6.6 0 1 .4 1 1V20c0 .6-.4 1-1 1A17 17 0 0 1 3 4c0-.6.4-1 1-1h3.5c.6 0 1 .4 1 1 0 1.3.2 2.5.6 3.6.1.3 0 .7-.2 1z"/></svg>
      123 - 456 - 7890
    </span>
  </div>
</header>

<nav class="wrap nav">
  <ul>
    <li class="active">HOME</li><li>ABOUT US</li><li>SANITIZERS</li><li>ALL PURPOSE CLEANERS</li><li>SOAPS</li><li>ALL NATURAL STUFF</li><li>CONTACT US</li>
  </ul>
  <svg class="search" width="16" height="16" viewBox="0 0 24 24"><circle cx="10" cy="10" r="7" fill="none" stroke="#fff" stroke-width="2.5"/><path d="M15 15l6 6" stroke="#fff" stroke-width="2.5"/></svg>
</nav>

<section class="wrap hero">
  <div class="hero-main">
    <div class="photo" role="img" aria-label="Row of foaming hand sanitizer bottles on a light surface"></div>
    <div class="copy">
      <span class="tag">NATURALLY FRESH</span>
      <h1>Hand Sanitizer</h1>
      <div class="sub">ALCOHOL FREE, FRAGRANCE FREE</div>
      <span class="btn">BUY NOW</span>
    </div>
    <div class="hero-dots"><span class="on"></span><span></span><span></span></div>
  </div>
  <div class="side side-a">
    <div class="txt"><div class="small">ALL PURPOSE CLEANER</div><div class="big">Up to 50% Off</div></div>
  </div>
  <div class="side side-b" role="img" aria-label="Natural soap bars with herbs on a wooden board"><div class="cap">ALL NATURAL STUFF</div></div>
  <div class="side side-c">
    <div class="big">SAVE 10%</div>
    <div class="code">GET YOUR FREE PROMO CODE NOW</div>
  </div>
</section>

<div class="wrap cats-bg"></div>
<h2 class="section-title" style="top:562px">Most Popular Categories</h2>
<div class="cats">
  <div class="cat">
    <div class="photo" role="img" aria-label="Hand sanitizer bottles"></div>
    <div class="icon"><svg width="14" height="14" viewBox="0 0 24 24"><path d="M5 12l5 5 9-10" stroke="#fff" stroke-width="3" fill="none"/></svg></div>
    <h3>SANITIZERS</h3><p>Up to 50%</p>
  </div>
  <div class="cat">
    <div class="photo" role="img" aria-label="All purpose cleaner spray bottles"></div>
    <div class="icon"><svg width="14" height="14" viewBox="0 0 24 24"><path d="M5 12l5 5 9-10" stroke="#fff" stroke-width="3" fill="none"/></svg></div>
    <h3>ALL PURPOSE CLEANERS</h3><p>Up to 50%</p>
  </div>
  <div class="cat feature">
    <div class="photo" role="img" aria-label="Handmade soap bars with flowers"></div>
    <div class="icon"><svg width="14" height="14" viewBox="0 0 24 24"><path d="M5 12l5 5 9-10" stroke="#fff" stroke-width="3" fill="none"/></svg></div>
    <h3>SOAPS</h3><p>Up to 50%</p>
    <span class="btn">SHOP NOW</span>
  </div>
  <div class="cat">
    <div class="photo" role="img" aria-label="Natural ingredients in jars with greenery"></div>
    <div class="icon"><svg width="14" height="14" viewBox="0 0 24 24"><path d="M5 12l5 5 9-10" stroke="#fff" stroke-width="3" fill="none"/></svg></div>
    <h3>ALL NATURAL STUFF</h3><p>Up to 50%</p>
  </div>
</div>

<h2 class="section-title" style="top:1100px">Featured Product</h2>
<div class="arrow" style="left:112px"><svg width="10" height="10" viewBox="0 0 10 10"><path d="M7 1L3 5l4 4" stroke="#fff" stroke-width="2" fill="none"/></svg></div>
<div class="arrow" style="left:1062px"><svg width="10" height="10" viewBox="0 0 10 10"><path d="M3 1l4 4-4 4" stroke="#fff" stroke-width="2" fill="none"/></svg></div>
<div class="products">
  <div class="prod"><span class="badge new">NEW</span>
    <div class="photo" role="img" aria-label="Set of hand sanitizer bottles"></div>
    <h4>GENTLE FOAMING HAND SANITIZER, 250ML</h4>
    <div class="price">$29.00<s>$35.00</s></div>
    <div class="actions"><span class="buy">BUY NOW</span><span class="wish"><svg width="12" height="12" viewBox="0 0 24 24"><path d="M12 21l-8-8a5 5 0 0 1 8-6 5 5 0 0 1 8 6z" fill="none" stroke="#1a8fd6" stroke-width="2.5"/></svg></span></div>
  </div>
  <div class="prod hover">
    <div class="photo" role="img" aria-label="Pair of sanitizer pump bottles"></div>
    <h4>GENTLE FOAMING HAND SANITIZER, 250ML</h4>
    <div class="price">$14.75<s>$19.00</s></div>
    <div class="actions"><span class="buy" style="background:var(--blue)">BUY NOW</span><span class="wish"><svg width="12" height="12" viewBox="0 0 24 24"><path d="M12 21l-8-8a5 5 0 0 1 8-6 5 5 0 0 1 8 6z" fill="none" stroke="#1a8fd6" stroke-width="2.5"/></svg></span></div>
  </div>
  <div class="prod">
    <div class="photo" role="img" aria-label="Sanitizer spray and refill bottles"></div>
    <h4>GENTLE FOAMING HAND SANITIZER, 250ML</h4>
    <div class="price">$28.00<s>$32.00</s></div>
    <div class="actions"><span class="buy">BUY NOW</span><span class="wish"><svg width="12" height="12" viewBox="0 0 24 24"><path d="M12 21l-8-8a5 5 0 0 1 8-6 5 5 0 0 1 8 6z" fill="none" stroke="#1a8fd6" stroke-width="2.5"/></svg></span></div>
  </div>
  <div class="prod"><span class="badge sale">SALE</span>
    <div class="photo" role="img" aria-label="Three all purpose cleaner bottles"></div>
    <h4>GENTLE FOAMING HAND SANITIZER, 250ML</h4>
    <div class="price">$24.75<s>$29.00</s></div>
    <div class="actions"><span class="buy">BUY NOW</span><span class="wish"><svg width="12" height="12" viewBox="0 0 24 24"><path d="M12 21l-8-8a5 5 0 0 1 8-6 5 5 0 0 1 8 6z" fill="none" stroke="#1a8fd6" stroke-width="2.5"/></svg></span></div>
  </div>
  <div class="prod">
    <div class="photo" role="img" aria-label="Refill pouch of natural cleaner"></div>
    <h4>GENTLE FOAMING HAND SANITIZER, 250ML</h4>
    <div class="price">$30.75<s>$36.00</s></div>
    <div class="actions"><span class="buy">BUY NOW</span><span class="wish"><svg width="12" height="12" viewBox="0 0 24 24"><path d="M12 21l-8-8a5 5 0 0 1 8-6 5 5 0 0 1 8 6z" fill="none" stroke="#1a8fd6" stroke-width="2.5"/></svg></span></div>
  </div>
</div>

<section class="wrap promo-band">
  <div class="left">
    <div class="mark"></div>
    <h2>HAND SANITIZER</h2>
    <div class="sub">Fragrance Free</div>
    <div class="flat">FLAT</div>
    <div class="off">40% Off</div>
    <span class="btn">BUY NOW</span>
  </div>
  <div class="right" role="img" aria-label="Hand sanitizer pump bottle on a wooden table"></div>
  <div class="inset" role="img" aria-label="Sanitizer bottles on a dark shelf"></div>
</section>

<div class="features">
  <div class="feat"><div class="ic"><svg width="40" height="30" viewBox="0 0 40 30"><rect x="2" y="6" width="22" height="16" fill="none" stroke="#7b858d" stroke-width="2"/><path d="M24 11h8l6 6v5H24z" fill="none" stroke="#7b858d" stroke-width="2"/><circle cx="10" cy="25" r="3" fill="#7cb82f"/><circle cx="31" cy="25" r="3" fill="#7cb82f"/></svg></div><h5>FREE SHIPPING</h5><p>for all orders over $99</p></div>
  <div class="feat"><div class="ic"><svg width="34" height="34" viewBox="0 0 34 34"><rect x="4" y="8" width="26" height="22" fill="none" stroke="#7b858d" stroke-width="2"/><path d="M10 18l5 5 9-10" stroke="#7cb82f" stroke-width="3" fill="none"/></svg></div><h5>OFFICIAL STOCK</h5><p>all natural and certified</p></div>
  <div class="feat"><div class="ic"><svg width="24" height="36" viewBox="0 0 24 36"><rect x="9" y="2" width="6" height="6" fill="#7b858d"/><rect x="4" y="10" width="16" height="24" rx="3" fill="none" stroke="#7b858d" stroke-width="2"/><rect x="7" y="18" width="10" height="8" fill="#7cb82f"/></svg></div><h5>2 FREE SAMPLES</h5><p>on all orders over $99</p></div>
  <div class="feat"><div class="ic"><svg width="34" height="34" viewBox="0 0 34 34"><circle cx="17" cy="17" r="14" fill="none" stroke="#1a8fd6" stroke-width="3"/><path d="M10 17l5 5 9-10" stroke="#7cb82f" stroke-width="3" fill="none"/></svg></div><h5>TRUSTED STORE</h5><p>rated 4.9 of 5 stars</p></div>
</div>

<footer class="wrap footer">
  <div class="brand"><span class="dot"></span><span class="name">Bright Leaf Northern</span></div>
  <div class="col" style="left:470px">
    <h6>CONTACT US</h6>
    <div class="call">CALL US: 123 - 456 - 7890</div>
    <div class="mail">brightleafnorthern@mailbox-example.com</div>
    <div class="connect">CONNECT WITH US</div>
    <div class="social"><span></span><span class="on"></span><span></span></div>
  </div>
  <div class="col news" style="left:780px">
    <h6>NEWSLETTER</h6>
    <p>Receive natural living tips, seasonal offers and product news in your inbox.</p>
    <div class="input">Enter Your Email</div>
    <span class="btn send">SEND</span>
  </div>
</footer>
<div class="wrap bottom">
  <div class="copy">© 2024 Bright Leaf Northern. All Rights Reserved.</div>
  <div class="pay"><span></span><span></span><span></span><span></span></div>
</div>
<div class="to-top"><svg width="10" height="10" viewBox="0 0 10 10"><path d="M1 7l4-4 4 4" stroke="#fff" stroke-width="2" fill="none"/></svg></div>

</body>
</html>
```